Brinmore Sports Pub. Where the locals go!!

We are creating a sports pub. We are needing a fun website that offers our menu along with an event page and general info. We have some attached links that we really like:
https://www.dolvetts.example/
https://www.cafemiralto.example/
https://www.quillstonepx.example/
We are doing a pirate theme but that is because the area we are in. We would like to see a pirate like in our logo doing something like drinking real time similar to the dolvetts website above.
Target Market(s)
Sports Fans
Industry/Entity Type
Pub, Bar, Restaurant
Coding
Coded - Design and coding required
Number of Pages Required
3 page
Font styles to use
Other font styles liked:
- see uploads
Look and feel

```html
<!DOCTYPE html>
<html lang="en">
<head>
<meta charset="utf-8">
<title>Brinmore Sports Pub</title>
<link href="https://fonts.googleapis.com/css2?family=Rye&family=Oswald:wght@500&family=Lato:wght@400&display=swap" rel="stylesheet">
<style>
:root{
  --red:#d8261c;
  --red-deep:#a8261b;
  --red-band:#b9301f;
  --cream:#faf5e8;
  --ink:#222222;
  --muted:#777068;
  --white:#ffffff;
  --black:#0d0d0d;
  --photo-warm:#6a3a24;
  --photo-dark:#2a1d18;
}
*{box-sizing:border-box;margin:0;padding:0}
html,body{width:1200px;height:3053px;overflow:hidden}
body{position:relative;background:var(--cream);font-family:'Lato',sans-serif;color:var(--ink)}
.abs{position:absolute}
.display{font-family:'Rye',serif;text-transform:uppercase}
.btn{position:absolute;display:flex;align-items:center;justify-content:center;border-radius:30px;font-family:'Rye',serif;text-transform:uppercase;font-size:19px;letter-spacing:1px;box-shadow:0 4px 8px rgba(0,0,0,.25)}
.btn-red{background:var(--red);color:var(--white)}
.btn-white{background:var(--white);color:var(--red)}

/* hero */
.hero{left:0;top:0;width:1200px;height:684px;background:linear-gradient(180deg,#2b1f1c 0%,#4a2c22 45%,#6b3c28 80%,#3b2520 100%)}
.site-header{left:98px;top:0;width:1002px;height:83px;background:var(--cream);border-radius:0 0 30px 30px}
.brand{left:98px;top:0;width:140px;height:124px;background:var(--cream);border-radius:0 0 70px 70px;display:flex;align-items:center;justify-content:center;text-align:center}
.brand span{font-family:'Rye',serif;color:var(--red);font-size:15px;line-height:19px;text-transform:uppercase;width:110px}
.nav{left:314px;top:30px;display:flex;gap:38px;font-family:'Rye',serif;text-transform:uppercase;font-size:16px;letter-spacing:1px;color:#3a3a3a}
.nav .on{color:var(--red)}
.hero-kicker{left:0;width:1200px;top:150px;text-align:center;color:var(--red);font-size:30px}
.hero-title{left:0;width:1200px;top:206px;text-align:center;color:var(--white);font-size:54px;letter-spacing:2px}

/* menu */
.section-title{left:0;width:1200px;text-align:center;font-size:50px;letter-spacing:2px}
.tab{position:absolute;top:827px;width:121px;height:49px;border-radius:25px;background:var(--white);display:flex;align-items:center;justify-content:center;font-family:'Oswald',sans-serif;font-size:19px;letter-spacing:1.5px;color:var(--ink)}
.tab.on{background:var(--red);color:var(--white)}
.dish{position:absolute;top:914px;width:231px;height:309px;background:var(--white);border-radius:22px;box-shadow:0 2px 8px rgba(0,0,0,.08)}
.dish .pic{position:absolute;left:10px;top:14px;width:211px;height:196px;border-radius:18px}
.dish h3{position:absolute;left:16px;top:223px;font-family:'Oswald',sans-serif;font-weight:500;font-size:16px}
.dish p{position:absolute;left:16px;top:250px;width:170px;font-size:11.5px;line-height:21px;color:var(--muted)}
.dish .fav{position:absolute;right:12px;top:228px;width:28px;height:28px;border-radius:50%;background:#f1eee8}
.dish .fav svg{position:absolute;left:7px;top:7px}

/* about */
.about{left:0;top:1390px;width:1200px;height:673px;background:radial-gradient(ellipse at 60% 40%,#c4372a 0%,var(--red-band) 55%,var(--red-deep) 100%)}
.about-pic{left:110px;top:1563px;width:426px;height:551px;border:2px solid var(--white);border-radius:140px 0 140px 0;background:linear-gradient(160deg,#8e2a1e 0%,#5a2a1e 45%,#2e1c16 100%)}
.about-copy{left:620px;top:1557px;width:475px;color:var(--white);font-size:15px;line-height:29px}
.about-copy p+p{margin-top:29px}

/* events */
.event{position:absolute;top:2257px;width:298px;height:255px}
.event .pic{width:298px;height:205px;border-radius:0 0 18px 0}
.event .label{position:absolute;left:23px;top:178px;width:254px;height:77px;background:var(--cream);border-radius:14px 14px 0 0;text-align:center;padding-top:12px}
.event h3{font-family:'Oswald',sans-serif;font-weight:500;font-size:19px;color:var(--ink)}
.event p{font-size:13px;color:var(--red);margin-top:6px}
.arrow{position:absolute;top:2371px;width:36px;height:36px;border-radius:50%;background:var(--red)}
.arrow svg{position:absolute;left:9px;top:9px}

/* footer */
.footer{left:0;top:2585px;width:1200px;height:468px;background:var(--black)}
.foot-brand{left:528px;top:2653px;width:144px;height:144px;border-radius:50%;background:var(--white);display:flex;align-items:center;justify-content:center;text-align:center}
.foot-brand span{font-family:'Rye',serif;color:var(--red);font-size:15px;line-height:19px;text-transform:uppercase;width:110px}
.foot-nav{left:0;width:1200px;top:2836px;display:flex;justify-content:center;gap:38px;font-family:'Rye',serif;text-transform:uppercase;font-size:16px;letter-spacing:1px;color:var(--white)}
.contact{position:absolute;top:2900px;display:flex;align-items:center;gap:12px;font-family:'Rye',serif;text-transform:uppercase;font-size:14px;letter-spacing:1px;color:var(--white)}
.contact i{display:block;width:36px;height:36px;border:2px solid var(--white);border-radius:50%;position:relative}
.contact i svg{position:absolute;left:8px;top:8px}
.copyright{left:0;width:1200px;top:2980px;text-align:center;font-family:'Rye',serif;text-transform:uppercase;font-size:13px;letter-spacing:1px;color:var(--white)}
</style>
</head>
<body>

<section class="abs hero" role="img" aria-label="Photo of sports fans cheering at a crowded bar in front of screens showing a football game"></section>
<header>
  <div class="abs site-header"></div>
  <div class="abs brand"><span>Brinmore Sports Pub</span></div>
  <nav class="abs nav">
    <span class="on">Home</span><span>About</span><span>Our Menu</span><span>Event</span><span>Testimonials</span>
  </nav>
  <div class="btn btn-red" style="left:901px;top:20px;width:157px;height:43px;font-size:16px">Contact Us</div>
</header>
<div class="abs display hero-kicker">Welcome to</div>
<h1 class="abs display hero-title">Brinmore Sports Pub</h1>
<div class="btn btn-red" style="left:493px;top:299px;width:215px;height:54px">Get Started</div>

<h2 class="abs display section-title" style="top:748px;color:var(--red)">Our Menu</h2>
<div class="tab" style="left:382px">Drinks</div>
<div class="tab on" style="left:540px">Cocktail</div>
<div class="tab" style="left:697px">Juice</div>

<article class="dish" style="left:95px">
  <div class="pic" role="img" aria-label="Photo of an old fashioned cocktail" style="background:linear-gradient(160deg,#3a2416,#9a5a22 60%,#2a1a12)"></div>
  <h3>Old Fashioned Cocktail</h3>
  <p>Excepteur sint occaecat cupidat at non proident, sunt in culpa</p>
  <span class="fav"><svg width="14" height="14" viewBox="0 0 24 24"><path d="M12 21s-8-5.3-8-11a4.5 4.5 0 0 1 8-2.8A4.5 4.5 0 0 1 20 10c0 5.7-8 11-8 11z" fill="none" stroke="#222" stroke-width="2"/></svg></span>
</article>
<article class="dish" style="left:356px">
  <div class="pic" role="img" aria-label="Photo of a negroni in a cut glass" style="background:linear-gradient(160deg,#1a1412,#b8482c 55%,#1c1210)"></div>
  <h3>Negroni</h3>
  <p>Duis aute irure dolor in reprehenderit in voluptate velit</p>
  <span class="fav"><svg width="14" height="14" viewBox="0 0 24 24"><path d="M12 21s-8-5.3-8-11a4.5 4.5 0 0 1 8-2.8A4.5 4.5 0 0 1 20 10c0 5.7-8 11-8 11z" fill="none" stroke="#222" stroke-width="2"/></svg></span>
</article>
<article class="dish" style="left:617px">
  <div class="pic" role="img" aria-label="Photo of a whiskey sour with a cherry" style="background:linear-gradient(160deg,#2a2622,#d8a23a 55%,#3a3430)"></div>
  <h3>Whiskey Sour</h3>
  <p>Excepteur sint occaecat cupidat at non proident, sunt in culpa</p>
  <span class="fav"><svg width="14" height="14" viewBox="0 0 24 24"><path d="M12 21s-8-5.3-8-11a4.5 4.5 0 0 1 8-2.8A4.5 4.5 0 0 1 20 10c0 5.7-8 11-8 11z" fill="none" stroke="#222" stroke-width="2"/></svg></span>
</article>
<article class="dish" style="left:877px">
  <div class="pic" role="img" aria-label="Photo of a dry martini with a lime slice" style="background:linear-gradient(160deg,#1e1e1c,#8c9a6a 55%,#262420)"></div>
  <h3>Dry Martini</h3>
  <p>Duis aute irure dolor in reprehenderit in voluptate velit</p>
  <span class="fav"><svg width="14" height="14" viewBox="0 0 24 24"><path d="M12 21s-8-5.3-8-11a4.5 4.5 0 0 1 8-2.8A4.5 4.5 0 0 1 20 10c0 5.7-8 11-8 11z" fill="none" stroke="#222" stroke-width="2"/></svg></span>
</article>
<div class="btn btn-red" style="left:502px;top:1271px;width:198px;height:55px">View More</div>

<section class="abs about"></section>
<h2 class="abs display section-title" style="top:1464px;color:var(--white)">About Brinmore Sports Pub</h2>
<div class="abs about-pic" role="img" aria-label="Photo of guests at tables inside the pub under red lights and hanging decor"></div>
<div class="abs about-copy">
  <p>At vero eos et accusamus et iusto odio dignissimos ducimus qui bla tiis praesentium voluptatum deleniti atque corrupti quos dolores et quas molestias excepturi sint occaecati cupiditate non provident, similique sunt in culpa qui officia deserunt mollitia animi, id est laborum et dolor um fuga. Nam libero tempore, cum soluta nobis est eligendi optio cum que nihil impedit quo minus id quod maxime placeat facere possimus, omnis voluptas assumenda est, omnis dolor repellendus. Temporibus ptates repudiandae sint et molestiae non recusandae.</p>
  <p>Itaque earum rerum hic tenetur a sapiente delectus, ut aut reiciendis voluptatibus maiores alias consequatur aut perferendis doloribus asperiores repellat.</p>
</div>
<div class="btn btn-white" style="left:620px;top:1933px;width:197px;height:54px">Read More</div>

<h2 class="abs display section-title" style="top:2170px;color:var(--red)">Our Events</h2>
<span class="arrow" style="left:38px"><svg width="18" height="18" viewBox="0 0 24 24"><path d="M20 12H5M11 5l-7 7 7 7" fill="none" stroke="#fff" stroke-width="3"/></svg></span>
<article class="event" style="left:110px">
  <div class="pic" role="img" aria-label="Photo of a long wooden bar with screens above" style="background:linear-gradient(180deg,#5a5a62,#7a4a26 55%,#3a2418)"></div>
  <div class="label"><h3>Temporibus autem</h3><p>Rerum necessitatibus saepe eveniet</p></div>
</article>
<article class="event" style="left:451px">
  <div class="pic" role="img" aria-label="Photo of a brick-walled lounge with framed jerseys" style="background:linear-gradient(180deg,#3a2a22,#7a3e28 55%,#2a1e18)"></div>
  <div class="label"><h3>Itaque earum rerum</h3><p>Voluptatibus maiores alias conseur</p></div>
</article>
<article class="event" style="left:791px">
  <div class="pic" role="img" aria-label="Photo of a colourful bar covered in flags and signs" style="background:linear-gradient(180deg,#a83a2e,#c88a2a 50%,#3a2a2a)"></div>
  <div class="label"><h3>Nam libero tempore</h3><p>Quod maxime placeat facere</p></div>
</article>
<span class="arrow" style="left:1126px"><svg width="18" height="18" viewBox="0 0 24 24"><path d="M4 12h15M13 5l7 7-7 7" fill="none" stroke="#fff" stroke-width="3"/></svg></span>

<footer>
  <div class="abs footer"></div>
  <div class="abs foot-brand"><span>Brinmore Sports Pub</span></div>
  <nav class="abs foot-nav"><span>Home</span><span>About</span><span>Our Menu</span><span>Event</span><span>Testimonials</span><span>Contact Us</span></nav>
  <div class="contact" style="left:153px"><i><svg width="16" height="16" viewBox="0 0 24 24"><path d="M12 22s7-7 7-12a7 7 0 0 0-14 0c0 5 7 12 7 12z" fill="none" stroke="#fff" stroke-width="2"/><circle cx="12" cy="10" r="2.5" fill="#fff"/></svg></i>Brinmore Sports Pub, US</div>
  <div class="contact" style="left:491px"><i><svg width="16" height="16" viewBox="0 0 24 24"><rect x="3" y="5" width="18" height="14" rx="2" fill="#fff"/><path d="M3 6l9 7 9-7" fill="none" stroke="#0d0d0d" stroke-width="2"/></svg></i>info@brinmoresports.example</div>
  <div class="contact" style="left:870px"><i><svg width="16" height="16" viewBox="0 0 24 24"><path d="M5 3h4l2 5-3 2a11 11 0 0 0 6 6l2-3 5 2v4a2 2 0 0 1-2 2A17 17 0 0 1 3 5a2 2 0 0 1 2-2z" fill="none" stroke="#fff" stroke-width="2"/></svg></i>+1 555 014 2290</div>
  <div class="abs copyright">Copyrights © 2023. Brinmore Sports Pub. All Rights Reserved</div>
</footer>

</body>
</html>
```